Natural Health Supplement Company Needs a Product Label Designed

HARVEST ROOT LABS needs a PROBIOTICS product label designed.We are a natural health vitamin and dietary supplement company. Who ever wins will have the opportunity to design a lot more product labels for us.
Product name: PROBIOTICS
*Please use the attached logo and base the label text exactly off the Kelt Wellness label example.
Other product examples have been attached for inspiration.

Colors

Designer to choose colors to be used in the design.

Requirements
Must have
• Product name: PROBIOTICS
• *Please use the attached logo and base the label text exactly off the Kelt Wellness label example.
• Other product examples have been attached for inspiration.

```html
<!DOCTYPE html>
<html lang="en">
<head>
<meta charset="UTF-8">
<title>Harvest Root Labs – Probiotic-40 Label</title>
<link rel="stylesheet" href="https://fonts.googleapis.com/css2?family=Montserrat:wght@400;600;800&display=swap">
<style>
  :root {
    --stage: #dedcab;
    --label-light: #f5f8e4;
    --label-mid: #e8efc7;
    --label-edge: #bcc39a;
    --ink: #555555;
    --ink-soft: #666666;
    --green: #5fb53a;
    --green-soft: #6cbd45;
  }
  * { margin: 0; padding: 0; box-sizing: border-box; }
  html, body {
    width: 1200px;
    height: 900px;
    overflow: hidden;
  }
  body {
    background: var(--stage);
    display: flex;
    align-items: center;
    justify-content: center;
    font-family: "Montserrat", sans-serif;
  }
  .label {
    width: 600px;
    height: 720px;
    background: linear-gradient(90deg, var(--label-edge) 0%, var(--label-mid) 12%, var(--label-light) 45%, var(--label-mid) 82%, var(--label-edge) 100%);
    display: flex;
    flex-direction: column;
    align-items: center;
    text-align: center;
    padding-top: 110px;
  }
  .brand {
    display: flex;
    align-items: center;
    gap: 12px;
  }
  .brand-dot {
    width: 18px;
    height: 18px;
    border-radius: 50%;
    background: var(--green);
  }
  .brand-name {
    font-weight: 600;
    font-size: 30px;
    letter-spacing: 2px;
    color: var(--green);
  }
  .product-name {
    margin-top: 88px;
    font-weight: 800;
    font-size: 50px;
    line-height: 1.1;
    color: var(--ink);
  }
  .technology {
    margin-top: 40px;
    color: var(--green-soft);
  }
  .technology-mark {
    display: flex;
    align-items: center;
    justify-content: center;
    gap: 14px;
    font-size: 36px;
    font-weight: 400;
    letter-spacing: 1px;
  }
  .technology-mark sup { font-size: 16px; }
  .technology-mark .accent {
    width: 12px;
    height: 12px;
    border-radius: 50%;
    background: var(--green);
  }
  .technology-line {
    font-size: 35px;
    font-weight: 400;
    margin-top: 2px;
  }
  .offer {
    margin-top: 115px;
    color: var(--ink);
  }
  .offer-title {
    font-weight: 800;
    font-size: 34px;
    letter-spacing: 0.5px;
  }
  .offer-line {
    font-weight: 400;
    font-size: 35px;
    color: var(--ink-soft);
    margin-top: 2px;
  }
</style>
</head>
<body>
  <main class="label">
    <div class="brand">
      <span class="brand-dot"></span>
      <span class="brand-name">HARVEST ROOT LABS</span>
    </div>

    <h1 class="product-name">PROBIOTIC-40<br>40 BILLION</h1>

    <div class="technology">
      <div class="technology-mark">
        <span class="accent"></span>
        <span>VELLOCAP<sup>®</sup></span>
        <span class="accent"></span>
      </div>
      <div class="technology-line">Dual-Core Delivery</div>
    </div>

    <div class="offer">
      <div class="offer-title">PRIVATE LABELING</div>
      <div class="offer-line">Any Capsules Count</div>
    </div>
  </main>
</body>
</html>
```